Gleam - Advanced Laser Teeth Whitening

Gleam is a new teeth whitening business in a market that is not familar which this treatment.
The brochure needs to establish the brand (see logo) and be informative (see copy).
The service will be carried out at a home based clinic and a mobile service will also be available.
I've also attached some stock photos, please feel free to use these and the logo as you think appropriate.
Although many customers will be women, we want the style to also be accessable to men.
Reason: I'm going on business for the next few days so I am extending the deadline so that I can provide proper feedback.
Target Market(s)
All men and women over 18 and particularly women aged between 18 and 40.
Industry/Entity Type
Clinic
Requirements
Must have
- Logo - I have other formats if required - Please e-mail me - adamrussell@manx.netPhotos - I would like more photos that the ones attached, I have more please e-mail me.Uncluttered informative copyThe basic price on the front pageContact details on the back page'Copyright 2008 All Rights Reserved' on the back page
Nice to have
- Lots of white to reflect the business and it's clean, proffessional image.
Should not have
- An old fashioned, cluttered or unprofessional apprearance.

```html
<!DOCTYPE html>
<html lang="en">
<head>
<meta charset="utf-8">
<title>Gleam - Advanced Laser Teeth Whitening</title>
<link rel="stylesheet" href="https://fonts.googleapis.com/css2?family=Delius&family=PT+Sans:wght@400;700&display=swap">
<style>
  :root {
    --magenta: #f21bd0;
    --magenta-deep: #e010c2;
    --sun: #f4ee1c;
    --sun-soft: #f9f47a;
    --paper: #ffffff;
    --ink: #111111;
    --price: #f0161c;
    --skin-light: #f6dccd;
    --skin: #e9b79f;
    --hair: #9a6a45;
  }
  html, body {
    margin: 0;
    padding: 0;
    width: 849px;
    height: 1200px;
    overflow: hidden;
    background: var(--paper);
  }
  .brochure {
    position: relative;
    width: 849px;
    height: 1200px;
    overflow: hidden;
  }
  .brochure__art {
    display: block;
    width: 849px;
    height: 1200px;
  }
  .brand-name {
    font-family: "PT Sans", sans-serif;
    font-weight: 700;
    font-size: 112px;
    fill: var(--magenta);
  }
  .brand-tagline {
    font-family: "PT Sans", sans-serif;
    font-weight: 400;
    font-size: 24.5px;
    fill: var(--magenta);
  }
  .benefit {
    font-family: "Delius", cursive;
    font-size: 29px;
    fill: var(--ink);
  }
  .price {
    font-family: "Delius", cursive;
    font-size: 27px;
    fill: var(--price);
  }
  .badge-text {
    font-family: "Delius", cursive;
    font-size: 17px;
    fill: var(--paper);
  }
</style>
</head>
<body>
<main class="brochure">
  <svg class="brochure__art" viewBox="0 0 827 1169" preserveAspectRatio="none" xmlns="http://www.w3.org/2000/svg">
    <defs>
      <linearGradient id="portrait-tone" x1="0" y1="0" x2="1" y2="0.3">
        <stop offset="0" stop-color="var(--hair)"/>
        <stop offset="0.18" stop-color="var(--skin)"/>
        <stop offset="0.6" stop-color="var(--skin-light)"/>
        <stop offset="1" stop-color="var(--paper)"/>
      </linearGradient>
      <linearGradient id="field-tone" x1="0" y1="0" x2="0" y2="1">
        <stop offset="0" stop-color="var(--sun)"/>
        <stop offset="1" stop-color="var(--sun-soft)"/>
      </linearGradient>
    </defs>

    <!-- portrait area -->
    <g class="portrait" role="img" aria-label="Photo of a smiling woman with white teeth and sunflowers in her hair">
      <rect x="0" y="0" width="470" height="640" fill="url(#portrait-tone)"/>
    </g>

    <!-- top right sweep -->
    <path class="sweep sweep--top" d="M470,0 C640,40 780,120 827,222 L827,0 Z" fill="var(--magenta)"/>

    <!-- sunflower field band -->
    <g class="field-band" role="img" aria-label="Sunflower field background">
      <rect x="0" y="642" width="827" height="490" fill="url(#field-tone)"/>
    </g>

    <!-- white benefit stripes -->
    <g class="stripes" fill="var(--paper)" opacity="0.92">
      <rect x="0" y="712" width="827" height="56"/>
      <rect x="0" y="796" width="827" height="56"/>
      <rect x="0" y="880" width="827" height="56"/>
      <rect x="0" y="964" width="827" height="56"/>
      <rect x="0" y="1047" width="827" height="56"/>
    </g>

    <!-- bottom left sweep -->
    <path class="sweep sweep--bottom" d="M0,645 C40,880 230,1090 827,1169 L0,1169 Z" fill="var(--magenta)"/>

    <!-- brand -->
    <text class="brand-name" x="400" y="556">Gleam</text>
    <text class="brand-tagline" x="397" y="605">Advanced Laser Teeth Whitening</text>

    <!-- benefits -->
    <text class="benefit" x="124" y="752">Most advanced and safest technology</text>
    <text class="benefit" x="183" y="834">Immediate brilliant results</text>
    <text class="benefit" x="277" y="919">Non invasive and pain free</text>
    <text class="benefit" x="390" y="1003">Smile with confidence</text>
    <text class="price" x="527" y="1087">All for just £149 !</text>

    <!-- slogan badge -->
    <g class="slogan-badge">
      <circle cx="116" cy="1012" r="86" fill="none" stroke="var(--paper)" stroke-width="3"/>
      <text class="badge-text" text-anchor="middle">
        <tspan x="116" y="985">You’re never</tspan>
        <tspan x="116" y="1007">fully dressed</tspan>
        <tspan x="116" y="1029">without</tspan>
        <tspan x="116" y="1051">a smile!</tspan>
      </text>
    </g>
  </svg>
</main>
</body>
</html>
```